VELQ Coding Courses Email Marketing Campaign

We are looking for someone to provide 4 email campaigns to publish in the month of October. The campaign will be sent via postrively and must include an commerce solution, incorporate our commercial, brochure and registration form.
Important things to highlight in the design content:
NMBT Approved Education Provider
Enhanced curriculum with GROVEL domains
Affordable cost with payment plans
Name Brand Learning Management System- Tarnix
Flexible learning with instructor led or self paced courses
Job placement opportunities with VEL Wellpath Care Solutions
Industry/Entity Type
Marketing
Look and feel

```html
<!DOCTYPE html>
<html lang="en">
<head>
<meta charset="utf-8">
<title>VELQ Coding Courses</title>
<link href="https://fonts.googleapis.com/css2?family=Raleway:wght@500;600;700;800&family=Roboto:wght@400;500&display=swap" rel="stylesheet">
<style>
:root{
  --purple:#5f2295;
  --tile:#6b2d9b;
  --green:#75b62a;
  --grey-text:#8a8a8a;
  --dark-text:#555555;
  --panel:#ebebeb;
  --white:#ffffff;
  --rule:#dddddd;
}
*{margin:0;padding:0;box-sizing:border-box}
html,body{width:738px;height:1200px;overflow:hidden;background:var(--white)}
body{position:relative;font-family:"Roboto",Arial,sans-serif}
.abs{position:absolute}
.brand{left:0;width:738px;top:12px;text-align:center;font-family:"Raleway",sans-serif;font-weight:600;font-size:64px;line-height:80px;color:var(--purple);letter-spacing:1px}
.brand-rule{left:2px;width:736px;top:104px;height:4px;background:var(--green)}
.hero{left:2px;top:110px;width:736px;height:328px;
  background:radial-gradient(ellipse at 45% 45%,#e0318f 0%,#b0246b 25%,#6a3a4a 55%,#2a1d20 100%)}
.headline{left:0;width:738px;top:454px;text-align:center;font-family:"Raleway",sans-serif;font-weight:700;font-size:22px;color:#5a5a5a;letter-spacing:.3px}
.headline span{color:var(--green)}
.intro{left:150px;width:438px;top:486px;text-align:center;font-size:11px;line-height:19px;color:var(--grey-text)}
.cta{left:0;width:738px;top:548px;text-align:center;font-family:"Raleway",sans-serif;font-weight:700;font-size:15px;color:var(--purple)}
.why-panel{left:2px;top:583px;width:736px;height:422px;background:var(--panel)}
.why-title{left:0;width:738px;top:596px;text-align:center;font-family:"Raleway",sans-serif;font-weight:700;font-size:21px;color:var(--purple)}
.why-text{left:150px;width:438px;top:629px;text-align:center;font-size:11px;line-height:18px;color:var(--grey-text)}
.feature{width:139px;height:120px;background:var(--tile);color:#e6e0ee;text-align:center;font-family:"Raleway",sans-serif;font-weight:700;font-size:14px;line-height:16px}
.feature svg{position:absolute;left:47px;top:18px}
.feature p{position:absolute;left:0;right:0;bottom:12px}
.register{left:311px;top:961px;width:120px;height:29px;border-radius:15px;background:var(--green);color:var(--white);text-align:center;line-height:29px;font-family:"Raleway",sans-serif;font-weight:700;font-size:13px}
.brochure{left:0;width:738px;top:1019px;text-align:center;font-family:"Raleway",sans-serif;font-weight:600;font-size:13px;color:var(--green)}
.site{left:0;width:738px;top:1040px;text-align:center;font-family:"Raleway",sans-serif;font-weight:700;font-size:13px;color:var(--purple)}
.footer-rule{left:170px;width:400px;top:1068px;height:1px;background:var(--rule)}
.office-photo{left:154px;top:1080px;width:166px;height:103px;background:linear-gradient(135deg,#d8d8d8 0%,#8a8a8a 45%,#3b3b3b 100%)}
.contact{left:330px;top:1081px;font-size:11px;line-height:17px;color:var(--dark-text)}
.contact h3{font-family:"Raleway",sans-serif;font-weight:700;font-size:12px;color:var(--green)}
.contact b{color:var(--purple);font-weight:500}
.contact .follow{font-family:"Raleway",sans-serif;font-weight:700;font-size:12px;color:var(--green);margin-top:1px}
.social{display:flex;gap:4px;margin-top:2px}
.social i{display:block;width:18px;height:18px;border-radius:50%;background:#6d6d6d}
</style>
</head>
<body>
<div class="abs brand">VELQ</div>
<div class="abs brand-rule"></div>
<div class="abs hero" role="img" aria-label="Photo of a smiling woman in green sunglasses covered in bright festival colour powder"></div>

<h1 class="abs headline">START YOUR CODING <span>CAREER TODAY</span></h1>
<p class="abs intro">Coding is one of the fastest, growing careers in the industry today. An average salary of a coder is $50,000 with around 3 years of experience. Coders have the flexibility to work from home with endless advancement opportunities.</p>
<p class="abs cta">What are you waiting for?&nbsp; Enroll today!</p>

<section class="abs why-panel"></section>
<h2 class="abs why-title">WHY VEL?</h2>
<p class="abs why-text">We have invested a lot of time and resources to ensure our coding program not only prepares you to pass the test the first time but to be job ready.<br>Our next class starts October 31st.</p>

<svg width="0" height="0" style="position:absolute">
  <defs>
    <g id="stethoscope" fill="none" stroke="#ffffff" stroke-width="2" stroke-linecap="round">
      <path d="M6 4 C2 6 2 14 6 18 C9 21 13 21 16 18 C20 14 20 6 16 4"/>
      <path d="M11 20 V40 C11 50 26 50 26 40 V32"/>
      <circle cx="31" cy="28" r="4" fill="#ffffff" stroke="none"/>
    </g>
  </defs>
</svg>

<div class="abs feature" style="left:155px;top:692px"><svg width="44" height="56"><use href="#stethoscope"/></svg><p>NMBT APPROVED</p></div>
<div class="abs feature" style="left:302px;top:692px"><svg width="44" height="56"><use href="#stethoscope"/></svg><p>GROVEL DOMAINS</p></div>
<div class="abs feature" style="left:449px;top:692px"><svg width="44" height="56"><use href="#stethoscope"/></svg><p>PAYMENT PLANS</p></div>
<div class="abs feature" style="left:155px;top:820px"><svg width="44" height="56"><use href="#stethoscope"/></svg><p>JOB PLACEMENT</p></div>
<div class="abs feature" style="left:302px;top:820px"><svg width="44" height="56"><use href="#stethoscope"/></svg><p style="bottom:3px">FLEXBILE ONLINE COURSES</p></div>
<div class="abs feature" style="left:449px;top:820px"><svg width="44" height="56"><use href="#stethoscope"/></svg><p>LMS: TARNIX</p></div>

<div class="abs register">REGISTER</div>

<p class="abs brochure">Click here to download our brochure</p>
<p class="abs site">www.velwellpathcare.com</p>
<div class="abs footer-rule"></div>

<div class="abs office-photo" role="img" aria-label="Photo of the training centre lobby with a silver reception sign"></div>
<div class="abs contact">
  <h3>STILL HAVE QUESTIONS?</h3>
  <p>2180 Harlow Crest Drive, STE 210, Brenton, TX 75418</p>
  <p><b>Email :</b> velacademy@velwellpathcare.com</p>
  <p><b>Call :</b> (555) 318-2706</p>
  <p class="follow">Follow us</p>
  <div class="social"><i></i><i></i><i></i></div>
</div>
</body>
</html>
```